Workforce Equity Lens Poster for staff

Our organization has developed an equity lens to be used by staff when implementing new programs and services. We need a poster that will be used as a quick reference for staff to use on a daily basis and will hang in cubicles. We'd like the main six questions to stand out with the subsequent questions less prominent. Looking for a poster that is 11 x 17 inches.

Industry/Entity Type

Equity

Font styles to use
Sans Serif

Colors

Designer to choose colors to be used in the design.

Requirements
Must have
• Easy to read. Not too text heavy, so any way to highlight the main six questions. It would be great to have some sort of icon or illustration with each of the six questions.
Nice to have
• Illustrative design features.
Should not have
• No photos of people.

```html
<!DOCTYPE html>
<html lang="en">
<head>
<meta charset="utf-8">
<title>Workforce System Equity Lens – Poster Variants</title>
<link href="https://fonts.googleapis.com/css2?family=Montserrat:wght@500;600;700&family=Lato:wght@400;700&display=swap" rel="stylesheet">
<style>
  :root {
    --blue: #2f84c8;
    --blue-dark: #1f6fb0;
    --ink: #1c1c1c;
    --body: #2a2a2a;
    --page: #ffffff;
    --page-fade: #f1f2f3;
    --canvas: #ffffff;
  }
  * { box-sizing: border-box; margin: 0; padding: 0; }
  html, body { width: 1200px; height: 1200px; overflow: hidden; background: var(--canvas); }
  body { position: relative; font-family: "Lato", sans-serif; color: var(--body); }

  .poster {
    position: absolute; top: 189px; width: 533px; height: 822px;
    background: linear-gradient(180deg, var(--page) 40%, var(--page-fade) 100%);
    overflow: hidden;
  }
  .poster--detailed { left: 46px; }
  .poster--focused { left: 621px; }

  .hero-photo {
    position: absolute; left: 0; top: 0; width: 100%;
    background: linear-gradient(120deg, #c9ccc8 0%, #8d8f8c 30%, #5a6470 55%, #b7b0a8 80%, #e3e1dc 100%);
  }
  .poster--detailed .hero-photo { height: 263px; }
  .poster--focused .hero-photo { height: 295px; }

  .abs { position: absolute; }

  .section-title {
    font-family: "Lato", sans-serif; font-weight: 400; font-size: 15px;
    color: var(--ink); letter-spacing: 0.2px;
  }
  .lead-text { font-size: 7.6px; line-height: 10.8px; color: var(--body); }

  .lens-pill {
    position: absolute; background: var(--blue); color: #fff;
    border-radius: 30px; display: flex; align-items: center; justify-content: center;
    text-align: center; font-family: "Montserrat", sans-serif;
  }
  .poster--detailed .lens-pill {
    left: 63px; top: 496px; width: 407px; height: 28px;
    font-size: 14px; font-weight: 500; letter-spacing: 0.3px;
  }
  .poster--focused .lens-pill {
    left: 63px; top: 307px; width: 406px; height: 53px;
    font-size: 15.5px; font-weight: 700; line-height: 19px; letter-spacing: 0.4px;
  }

  .question { position: absolute; }
  .question-icon { position: absolute; left: 0; top: 0; width: 37px; height: 37px; }
  .question-body { position: absolute; left: 42px; top: 0; }
  .poster--detailed .question-title {
    font-size: 7.4px; text-transform: uppercase; color: var(--ink); margin-bottom: 5px;
  }
  .poster--detailed .question-text { font-size: 7px; line-height: 9.2px; color: var(--body); width: 208px; }
  .poster--focused .question-title {
    font-family: "Montserrat", sans-serif; font-weight: 700; font-size: 11.2px;
    line-height: 13.6px; color: var(--ink); text-transform: uppercase; margin-bottom: 7px;
  }
  .poster--focused .question-text {
    font-size: 10.8px; line-height: 13.8px; color: var(--body); width: 203px; text-align: justify;
  }

  .brand { position: absolute; left: 30px; display: flex; align-items: center; gap: 10px; }
  .poster .brand { top: 756px; }
  .brand-dot { width: 30px; height: 30px; border-radius: 50%; background: var(--blue); flex: none; }
  .brand-name {
    font-family: "Montserrat", sans-serif; font-weight: 700; color: var(--blue);
    font-size: 17px; line-height: 19px; letter-spacing: 0.2px;
  }
  .brand-name span { display: block; font-size: 10px; letter-spacing: 6.4px; line-height: 14px; }

  .contact { position: absolute; left: 364px; top: 751px; font-size: 8.6px; line-height: 12.6px; color: var(--ink); }
  .contact-row { display: flex; align-items: flex-start; gap: 6px; }
  .contact-row svg { width: 8px; height: 8px; margin-top: 2px; flex: none; }
  .contact-row .indent { padding-left: 14px; }

  .footer-band { position: absolute; left: 0; bottom: 0; width: 100%; height: 12px; background: var(--blue); }
</style>
</head>
<body>

<svg width="0" height="0" style="position:absolute" aria-hidden="true">
  <defs>
    <symbol id="icon-affected" viewBox="0 0 40 40">
      <circle cx="20" cy="20" r="20" fill="var(--blue)"/>
      <g fill="none" stroke="#fff" stroke-width="1.4">
        <circle cx="14" cy="16" r="3"/><circle cx="26" cy="16" r="3"/><circle cx="20" cy="13" r="3"/>
        <path d="M9 26c0-4 3-6 5-6s5 2 5 6M21 26c0-4 3-6 5-6s5 2 5 6"/>
        <path d="M11 30a12 12 0 0 0 18 0"/>
      </g>
    </symbol>
    <symbol id="icon-table" viewBox="0 0 40 40">
      <circle cx="20" cy="20" r="20" fill="var(--blue)"/>
      <g fill="#fff">
        <rect x="11" y="20" width="18" height="2.5"/><rect x="13" y="22.5" width="1.6" height="7"/><rect x="25.4" y="22.5" width="1.6" height="7"/>
        <circle cx="10" cy="14" r="2.4"/><rect x="8" y="17" width="4" height="8" rx="1"/>
        <circle cx="30" cy="14" r="2.4"/><rect x="28" y="17" width="4" height="8" rx="1"/>
        <circle cx="20" cy="12" r="2.2"/><rect x="18.2" y="15" width="3.6" height="4" rx="1"/>
      </g>
    </symbol>
    <symbol id="icon-barriers" viewBox="0 0 40 40">
      <circle cx="20" cy="20" r="20" fill="var(--blue)"/>
      <g fill="#fff" stroke="#fff" stroke-width="1.4">
        <circle cx="20" cy="11" r="2.6"/>
        <path d="M20 14v6M11 20h18M11 20v5M20 20v5M29 20v5" fill="none"/>
        <circle cx="11" cy="28" r="2.4"/><circle cx="20" cy="28" r="2.4"/><circle cx="29" cy="28" r="2.4"/>
      </g>
    </symbol>
    <symbol id="icon-strategy" viewBox="0 0 40 40">
      <circle cx="20" cy="20" r="20" fill="var(--blue)"/>
      <g fill="none" stroke="#fff" stroke-width="1.6" stroke-linecap="round">
        <path d="M8 18l4 4M12 18l-4 4M26 9l3 3M29 9l-3 3M28 24l4 4M32 24l-4 4"/>
        <circle cx="18" cy="28" r="2.6"/>
        <path d="M18 25c0-6 4-9 9-12M24 12l3 1-1 3"/>
      </g>
    </symbol>
    <symbol id="icon-consequences" viewBox="0 0 40 40">
      <circle cx="20" cy="20" r="20" fill="var(--blue)"/>
      <path d="M9 18a12 12 0 0 1 22 0" fill="none" stroke="#fff" stroke-width="1.6"/>
      <path d="M29 14l2 4 3-3" fill="none" stroke="#fff" stroke-width="1.6"/>
      <g fill="#fff"><circle cx="12" cy="25" r="3"/><circle cx="20" cy="25" r="3"/><circle cx="28" cy="25" r="3"/></g>
    </symbol>
    <symbol id="icon-measure" viewBox="0 0 40 40">
      <circle cx="20" cy="20" r="20" fill="var(--blue)"/>
      <g fill="#fff">
        <rect x="18" y="24" width="3" height="6"/><rect x="23" y="20" width="3" height="10"/><rect x="28" y="15" width="3" height="15"/>
        <circle cx="12" cy="11" r="2.3"/><path d="M10 14h4l1 7h-2l-1 8h-2l-1-8H8z"/>
      </g>
      <path d="M17 20l6-6 3 2 5-6" fill="none" stroke="#fff" stroke-width="1.4"/>
    </symbol>
    <symbol id="icon-pin" viewBox="0 0 10 10"><path d="M5 1a3 3 0 0 1 3 3c0 2-3 5-3 5S2 6 2 4a3 3 0 0 1 3-3z" fill="none" stroke="var(--blue)" stroke-width="1"/></symbol>
    <symbol id="icon-mail" viewBox="0 0 10 10"><rect x="1" y="2.5" width="8" height="5.5" fill="var(--blue)"/><path d="M1 2.5l4 3 4-3" fill="none" stroke="#fff" stroke-width=".7"/></symbol>
    <symbol id="icon-phone" viewBox="0 0 10 10"><rect x="2.5" y="1" width="5" height="8" rx="1" fill="none" stroke="var(--blue)" stroke-width="1"/></symbol>
  </defs>
</svg>

<!-- Detailed variant -->
<section class="poster poster--detailed">
  <div class="hero-photo" role="img" aria-label="Photo area: a team of colleagues talking around a table in a bright office"></div>

  <h2 class="section-title abs" style="left:18px;top:272px;">WHAT IS EQUITY?</h2>
  <p class="lead-text abs" style="left:18px;top:293px;width:496px;">In workforce development, equity is the notion that everyone has the opportunity to obtain quality, living wage employment or be placed in employment-related training regardless of their national origin, race, gender, sexual orientation, disability, first language or other distinguishing characteristic. Different approaches to delivery of workforce services may be necessary in order for each customer to achieve success in training or employment.</p>

  <h2 class="section-title abs" style="left:18px;top:359px;">WHAT IS AN EQUITY LENS?</h2>
  <p class="lead-text abs" style="left:18px;top:379px;width:240px;">An equity lens is a practical tool that will help ensure that policies, programs, decisions, or proposed actions in Alder County's workforce system result in equitable outcomes for all job seekers. This lens shall be used by the Alder Workforce Alliance Board of Directors and Executive Board when making policy decisions or decisions on how to allocate funding. It shall also be used by Alder Workforce Alliance staff, WorkPath Alder staff, and other workforce system partners when creating and implementing programs.</p>
  <p class="lead-text abs" style="left:274px;top:379px;width:240px;">The purpose of the equity lens is to provide a tool to assist the Board and staff with identifying potentially negative outcomes for policies, programs, decisions, or actions that could increase disparities for under-represented populations. An equity lens is not meant to be a road block to effectively delivering workforce services, but rather a mechanism to identify and remove systemic barriers for under-represented populations as it relates to workforce-related services.</p>

  <div class="lens-pill">ALDER COUNTY WORKFORCE SYSTEM EQUITY LENS</div>

  <div class="question" style="left:18px;top:539px;">
    <svg class="question-icon"><use href="#icon-affected"/></svg>
    <div class="question-body"><p class="question-title">Who is affected?</p><p class="question-text">Who are the groups affected by this policy, metric, program, decision, or proposed action? How will each group be affected? Is any group negatively affected in a disproportionate way?</p></div>
  </div>
  <div class="question" style="left:18px;top:606px;">
    <svg class="question-icon"><use href="#icon-table"/></svg>
    <div class="question-body"><p class="question-title">Are they at the table?</p><p class="question-text">How have you actively involved stakeholders who are also members of the communities affected by the policy, metric, program, decision, or proposed action?</p></div>
  </div>
  <div class="question" style="left:18px;top:669px;">
    <svg class="question-icon"><use href="#icon-barriers"/></svg>
    <div class="question-body"><p class="question-title">What are the barriers?</p><p class="question-text">What are the societal or organizational barriers that prevent a population from being successful?</p></div>
  </div>
  <div class="question" style="left:271px;top:539px;">
    <svg class="question-icon"><use href="#icon-strategy"/></svg>
    <div class="question-body"><p class="question-title">What are population-specific strategies?</p><p class="question-text">To address any inequities, do we have solutions that are tailored to work for the disproportionately affected groups? Have we used the 'Platinum Rule'?</p></div>
  </div>
  <div class="question" style="left:271px;top:606px;">
    <svg class="question-icon"><use href="#icon-consequences"/></svg>
    <div class="question-body"><p class="question-title">Are there unintended consequences?</p><p class="question-text">Does this policy, program, decision, or proposed action ignore or worsen existing disparities or produce other unintended consequences?</p></div>
  </div>
  <div class="question" style="left:271px;top:669px;">
    <svg class="question-icon"><use href="#icon-measure"/></svg>
    <div class="question-body"><p class="question-title">How do we measure success in a population-specific way?</p><p class="question-text">Describe how data about the policy, metric, program, decision, or proposed action, and its impact (positive or negative) on equitable access and outcomes, will be monitored and evaluated?</p></div>
  </div>

  <div class="brand"><span class="brand-dot"></span><p class="brand-name">ALDER WORKFORCE<span>ALLIANCE</span></p></div>
  <div class="contact">
    <div class="contact-row"><svg><use href="#icon-pin"/></svg><span>Address: 48 Birch Lane,</span></div>
    <div class="contact-row"><span class="indent">Suite 200</span></div>
    <div class="contact-row"><svg><use href="#icon-mail"/></svg><span>info@alderworkforce.org</span></div>
    <div class="contact-row"><svg><use href="#icon-phone"/></svg><span>+1 555 014 0220</span></div>
  </div>
  <div class="footer-band"></div>
</section>

<!-- Focused variant -->
<section class="poster poster--focused">
  <div class="hero-photo" role="img" aria-label="Photo area: a team of colleagues talking around a table in a bright office"></div>

  <div class="lens-pill">ALDER COUNTY WORKFORCE<br>SYSTEM EQUITY LENS</div>

  <div class="question" style="left:18px;top:379px;">
    <svg class="question-icon"><use href="#icon-affected"/></svg>
    <div class="question-body"><p class="question-title">Who is affected?</p><p class="question-text">Who are the groups affected by this policy, metric, program, decision, or proposed action? How will each group be affected? Is any group negatively affected in a disproportionate way?</p></div>
  </div>
  <div class="question" style="left:18px;top:495px;">
    <svg class="question-icon"><use href="#icon-table"/></svg>
    <div class="question-body"><p class="question-title">Are they at the table?</p><p class="question-text">How have you actively involved stakeholders who are also members of the communities affected by the policy, metric, program, decision, or proposed action?</p></div>
  </div>
  <div class="question" style="left:18px;top:623px;">
    <svg class="question-icon"><use href="#icon-barriers"/></svg>
    <div class="question-body"><p class="question-title">What are the barriers?</p><p class="question-text">What are the societal or organizational barriers that prevent a population from being successful?</p></div>
  </div>
  <div class="question" style="left:271px;top:379px;">
    <svg class="question-icon"><use href="#icon-strategy"/></svg>
    <div class="question-body"><p class="question-title">What are population-specific strategies?</p><p class="question-text">To address any inequities, do we have solutions that are tailored to work for the disproportionately affected groups? Have we used the 'Platinum Rule'?</p></div>
  </div>
  <div class="question" style="left:271px;top:495px;">
    <svg class="question-icon"><use href="#icon-consequences"/></svg>
    <div class="question-body"><p class="question-title">Are there unintended consequences?</p><p class="question-text">Does this policy, program, decision, or proposed action ignore or worsen existing disparities or produce other unintended consequences?</p></div>
  </div>
  <div class="question" style="left:271px;top:620px;">
    <svg class="question-icon"><use href="#icon-measure"/></svg>
    <div class="question-body"><p class="question-title" style="margin-bottom:0;">How do we measure success in a population-specific way?</p><p class="question-text">Describe how data about the policy, metric, program, decision, or proposed action, and its impact (positive or negative) on equitable access and outcomes, will be monitored and evaluated?</p></div>
  </div>

  <div class="brand"><span class="brand-dot"></span><p class="brand-name">ALDER WORKFORCE<span>ALLIANCE</span></p></div>
  <div class="contact">
    <div class="contact-row"><svg><use href="#icon-pin"/></svg><span>Address: 48 Birch Lane,</span></div>
    <div class="contact-row"><span class="indent">Suite 200</span></div>
    <div class="contact-row"><svg><use href="#icon-mail"/></svg><span>info@alderworkforce.org</span></div>
    <div class="contact-row"><svg><use href="#icon-phone"/></svg><span>+1 555 014 0220</span></div>
  </div>
  <div class="footer-band"></div>
</section>

</body>
</html>
```